VANTA website redesign

VANTA provides situational safety training and equipment to give people the knowledge and skills to keep themselves safe, be effective and confident in their jobs. We want to redesign our current website, vanta.co.nz, to make it look cleaner and more appealing. Our colour palette is grey, orange and red (of the logo). Our audience was traditionally government agencies, mainly staff in enforcement or compliance roles, but is increasingly anyone in a front facing role, including librarians, health sector and non-enforcement. We need to ensure we retain a feel of being the leading providers in this field, as well as appeal to wider audience.
The final design will feel clean, fresh, inviting and ensure the audience understands we are the leaders in this training field. We should emphasise both the face to face training and our increasing online portfolio.

```html
<!DOCTYPE html>
<html lang="en">
<head>
<meta charset="utf-8">
<title>VANTA – Situational Safety & Tactical Communications</title>
<link href="https://fonts.googleapis.com/css2?family=Rubik:wght@500;600;700&family=Poppins:wght@400;500;600&display=swap" rel="stylesheet">
<style>
:root{
  --orange:#f05a28;
  --red:#e31e24;
  --ink:#2b2b2b;
  --grey:#555;
  --soft:#f4f4f4;
  --line:#e2e2e2;
  --peach:#fbd9c9;
  --footer:#2e2e2e;
}
*{box-sizing:border-box;margin:0;padding:0}
html,body{width:1200px;height:5085px;overflow:hidden;background:#fff}
body{font-family:"Poppins",sans-serif;color:var(--ink)}
.page{position:relative;width:1200px;height:5085px;overflow:hidden}
.abs{position:absolute}
.h{font-family:"Rubik",sans-serif}

/* header */
.brand{position:absolute;left:88px;top:24px;font-family:"Rubik",sans-serif;font-weight:700;font-size:50px;color:var(--grey);letter-spacing:1px;display:flex;align-items:center;gap:10px}
.brand i{display:block;width:14px;height:14px;background:var(--red)}
.contact{position:absolute;top:22px;display:flex;align-items:center;gap:10px;font-size:14px;color:var(--red);font-weight:500}
.contact .ico{width:28px;height:28px;border:1.5px solid #888;border-radius:4px;display:flex;align-items:center;justify-content:center}
.login{position:absolute;left:1024px;top:14px;width:86px;height:40px;background:var(--red);color:#fff;border-radius:4px;font-size:14px;font-weight:600;display:flex;align-items:center;justify-content:center}
.nav{position:absolute;top:72px;right:88px;display:flex;gap:26px;font-size:14px;color:var(--ink)}
.nav .on{color:var(--orange);border-bottom:2px solid var(--orange)}

/* hero */
.hero{position:absolute;left:0;top:107px;width:1200px;height:545px;background:linear-gradient(135deg,#4c4a48,#2c2a29 55%,#5a5350)}
.hero h1{position:absolute;left:0;width:1200px;top:135px;text-align:center;color:#fff;font-family:"Rubik",sans-serif;font-weight:600;font-size:42px;line-height:48px}
.btn-fill{position:absolute;background:var(--orange);color:#fff;border-radius:4px;font-size:14px;font-weight:500;display:flex;align-items:center;justify-content:center}
.dots{position:absolute;left:86px;top:560px;display:flex;gap:8px}
.dots span{width:26px;height:26px;border-radius:50%;background:#777;display:flex;align-items:center;justify-content:center}
.dots span.on{background:var(--orange)}

/* service tiles */
.tile{position:absolute;width:448px;box-shadow:0 4px 0 var(--orange)}
.tile .ph{width:100%;height:100%}
.tile .lbl{position:absolute;left:16px;bottom:-30px;width:270px;background:#fff;padding:26px 24px 24px;font-family:"Rubik",sans-serif;font-weight:600;font-size:33px;line-height:40px;color:var(--orange);border-left:4px solid var(--orange)}

/* about */
.about-card{position:absolute;left:113px;top:1745px;width:574px;height:430px;background:#fff;box-shadow:0 6px 24px rgba(0,0,0,.14);padding:36px 32px}
.about-card h2{font-family:"Rubik",sans-serif;font-weight:600;font-size:29px;line-height:38px;color:var(--red)}
.about-card p{font-size:13px;line-height:22px;margin-top:20px}
.about-card p.strong{font-weight:600;margin-top:28px}
.btn-line{position:absolute;border:1.5px solid var(--orange);color:var(--orange);border-radius:4px;font-size:14px;font-weight:500;display:flex;align-items:center;justify-content:center;background:#fff}

.section-title{position:absolute;left:0;width:1200px;text-align:center;font-family:"Rubik",sans-serif;font-weight:600;font-size:34px;color:var(--orange)}

.ind{position:absolute;top:2576px;width:237px;text-align:center;font-size:14px;font-weight:500}
.ind .ph{height:174px;margin-bottom:14px}

.partner{position:absolute;top:3093px;width:233px;height:106px;background:#fff;border:1px solid var(--line);display:flex;align-items:center;justify-content:center;gap:14px}

.quote-card{position:absolute;left:539px;top:3283px;width:572px;height:428px;background:#fff;box-shadow:0 6px 24px rgba(0,0,0,.12);text-align:center}

.post{position:absolute;top:3948px;width:323px;height:395px;background:#fff;box-shadow:0 3px 14px rgba(0,0,0,.1)}
.post .ph{height:226px}
.post p{font-size:12px;line-height:20px;color:var(--grey);padding:22px 26px 0}
.post .meta{position:absolute;left:26px;bottom:34px;right:26px;display:flex;align-items:center;gap:14px;font-size:11px;color:var(--grey)}
.post .av{width:48px;height:48px;border-radius:50%;border:1px solid var(--line);display:flex;align-items:center;justify-content:center;font-family:"Rubik",sans-serif;font-weight:600;font-size:12px;color:var(--grey)}
.post .sq{margin-left:auto;width:24px;height:24px;background:var(--ink);border-radius:3px}

.footer{position:absolute;left:0;top:4560px;width:1200px;height:525px}
.fcol{position:absolute;top:4678px;font-size:13px;line-height:26px;color:#eee}
.fcol h4{font-family:"Rubik",sans-serif;font-weight:600;font-size:19px;color:var(--orange);margin-bottom:8px}
.fcol li{list-style:none}
.fcol li.on{color:var(--orange)}
.fnav{position:absolute;top:4953px;left:0;width:1200px;display:flex;justify-content:center;gap:30px;font-size:13px;color:#eee}
.fnav .on{color:var(--orange);border-bottom:2px solid var(--orange)}
.fcall{position:absolute;top:4986px;width:1200px;text-align:center;color:#fff;font-size:21px}
.fcall b{color:var(--orange)}
.bar{position:absolute;left:0;top:5053px;width:1200px;height:32px;background:var(--orange);color:#fff;font-size:11px;display:flex;align-items:center;padding:0 88px}
</style>
</head>
<body>
<div class="page">

<!-- header -->
<div class="brand">VANTA<i></i></div>
<div class="contact" style="left:614px">
  <span class="ico"><svg width="14" height="14" viewBox="0 0 24 24"><path d="M6 2l4 4-2 3a12 12 0 007 7l3-2 4 4-3 4C10 22 2 14 2 5z" fill="#666"/></svg></span>0800 555 210</div>
<div class="contact" style="left:774px">
  <span class="ico"><svg width="14" height="12" viewBox="0 0 24 18"><rect x="1" y="1" width="22" height="16" fill="#666"/><path d="M1 1l11 9 11-9" stroke="#fff" stroke-width="2" fill="none"/></svg></span>info@vanta.co.nz</div>
<svg class="abs" style="left:955px;top:14px" width="46" height="40" viewBox="0 0 46 40"><path d="M2 6h7l5 20h22l5-14H12" stroke="#444" stroke-width="3" fill="none"/><circle cx="17" cy="34" r="3" fill="#444"/><circle cx="33" cy="34" r="3" fill="#444"/><circle cx="24" cy="7" r="7" fill="var(--orange)"/><text x="24" y="11" font-size="10" fill="#fff" text-anchor="middle" font-family="Poppins">0</text></svg>
<div class="login">Login</div>
<nav class="nav"><span class="on">Home</span><span>About</span><span>Industries Served ▾</span><span>Training ▾</span><span>Online Training</span><span>Gear ▾</span><span>Advice</span><span>Contact</span></nav>

<!-- hero -->
<div class="hero" role="img" aria-label="Photo of a trainee with headphones learning at a laptop">
  <h1>The Situational Safety &amp;<br>Tactical Communications<br>Experts</h1>
  <div class="btn-fill" style="left:527px;top:313px;width:145px;height:36px">Contact Us</div>
  <div class="dots" style="top:455px"><span><svg width="10" height="10" viewBox="0 0 10 10"><path d="M7 1L3 5l4 4" stroke="#fff" stroke-width="2" fill="none"/></svg></span><span class="on"><svg width="10" height="10" viewBox="0 0 10 10"><path d="M3 1l4 4-4 4" stroke="#fff" stroke-width="2" fill="none"/></svg></span></div>
</div>
<svg class="abs" style="left:0;top:530px" width="1200" height="140" viewBox="0 0 1200 140"><path d="M0 110 C400 95 900 70 1200 20 L1200 60 C900 100 400 120 0 140Z" fill="var(--peach)"/><path d="M0 140 C400 120 900 100 1200 60 L1200 140Z" fill="#fff"/></svg>

<!-- service tiles -->
<div class="tile" style="left:128px;top:764px;height:351px"><div class="ph" role="img" aria-label="Audience seated at a face-to-face training seminar" style="background:linear-gradient(135deg,#c8c2bb,#6b6560)"></div><div class="lbl">Face-to-Face<br>Training</div></div>
<div class="tile" style="left:624px;top:685px;height:332px"><div class="ph" role="img" aria-label="Laptop showing an online training presenter" style="background:linear-gradient(135deg,#8a7560,#d8d6d2 60%,#b9b3ab)"></div><div class="lbl">Online<br>Training</div></div>
<div class="tile" style="left:128px;top:1196px;height:354px"><div class="ph" role="img" aria-label="Body-worn video camera clipped to a vest" style="background:linear-gradient(135deg,#bfd0dc,#8a8f8e 55%,#3e3b38)"></div><div class="lbl" style="padding:32px 24px">Gear</div></div>
<div class="tile" style="left:624px;top:1117px;height:334px"><div class="ph" role="img" aria-label="Two people discussing documents at a desk" style="background:linear-gradient(135deg,#2f3a4c,#5c6472 60%,#a9a49c)"></div><div class="lbl" style="padding:32px 24px">Advice</div></div>

<!-- about -->
<div class="abs" style="left:0;top:1662px;width:113px;height:460px;background:linear-gradient(180deg,#e7e4df,#cfcac4)" role="img" aria-label="Office background"></div>
<div class="abs" style="left:405px;top:1662px;width:795px;height:460px;background:linear-gradient(120deg,#d9d2c8,#6f87a8 55%,#c9c4bd)" role="img" aria-label="Man in a denim shirt working on a laptop"></div>
<div class="about-card">
  <h2>Stay safe - physically, emotionally<br>and professionally with VANTA</h2>
  <p class="strong">Dealing with people is not always easy - especially when there is the potential for conflict. VANTA's training programmes give you, or your staff, the knowledge and skills to stay safe, be effective and deal confidently and professionally with people - in any situation.</p>
  <p>What sets VANTA apart from other training providers is our training delivery. Our team of experienced, engaging instructors teach proven skills and techniques, using real-life examples, making training relevant, entertaining and effective for anyone in a front line role.</p>
  <div class="btn-line" style="left:32px;top:356px;width:128px;height:36px;font-size:13px">Read More</div>
</div>

<!-- promo -->
<div class="abs" style="left:290px;top:2282px;width:480px;text-align:center;font-size:19px;line-height:29px">
  <div class="h" style="color:var(--red);font-weight:600;font-size:22px">Christmas Special!</div>
  <div>Halo Personal Safety Lights</div>
  <div><b style="color:var(--red);font-weight:600">10% OFF</b> until Christmas. Check them out here.</div>
</div>
<div class="abs" style="left:795px;top:2268px;width:180px;height:120px;border-radius:14px;background:radial-gradient(circle at 50% 70%,#e31e24,#2b2b2b 60%)" role="img" aria-label="Personal safety light unit with red LEDs"></div>

<!-- industries -->
<div class="abs" style="left:0;top:2428px;width:1200px;height:513px;background:var(--soft)"></div>
<div class="section-title" style="top:2494px">Industries Served</div>
<div class="ind" style="left:89px"><div class="ph" role="img" aria-label="Columned government building" style="background:linear-gradient(180deg,#aab4bd,#6e6a63)"></div>Central Government</div>
<div class="ind" style="left:351px"><div class="ph" role="img" aria-label="Council officer speaking to a crowd" style="background:linear-gradient(135deg,#8a6f5c,#b9a48f)"></div>Local Government</div>
<div class="ind" style="left:612px;color:var(--orange)"><div class="ph" role="img" aria-label="Model houses on a table" style="background:linear-gradient(135deg,#9fbc7c,#c9a787 60%,#88a5b6)"></div>Property Management</div>
<div class="ind" style="left:874px"><div class="ph" role="img" aria-label="Wooden blocks with health symbols" style="background:linear-gradient(135deg,#d9c8be,#c89b86)"></div>Health</div>
<div class="btn-line" style="left:539px;top:2829px;width:121px;height:34px">View All</div>

<!-- partners -->
<div class="section-title" style="top:3018px">Trusted to Deliver</div>
<svg class="abs" style="left:70px;top:3138px" width="14" height="20" viewBox="0 0 14 20"><path d="M11 2L3 10l8 8" stroke="#f7b59c" stroke-width="2" fill="none"/></svg>
<svg class="abs" style="left:1113px;top:3138px" width="14" height="20" viewBox="0 0 14 20"><path d="M3 2l8 8-8 8" stroke="var(--orange)" stroke-width="2.5" fill="none"/></svg>
<div class="partner" style="left:99px"><span style="width:36px;height:36px;border-radius:50%;background:#9aa"></span><span style="width:130px;height:16px;background:#3b4a7a;border-radius:2px"></span></div>
<div class="partner" style="left:362px"><span style="width:90px;height:30px;background:#333;border-radius:2px"></span><span style="width:36px;height:46px;background:#c23"></span></div>
<div class="partner" style="left:625px"><span style="width:170px;height:26px;background:#444;border-radius:2px"></span></div>
<div class="partner" style="left:888px"><span style="width:40px;height:40px;border-radius:50%;background:#e3b21d"></span><span style="width:120px;height:20px;background:#1c3f8a;border-radius:2px"></span></div>

<!-- testimonial -->
<div class="abs" style="left:0;top:3336px;width:1200px;height:454px;background:linear-gradient(90deg,#c9cfd6,#7c8aa0 30%,#d9dde2 60%,#c8cdd3)" role="img" aria-label="Smiling businessman in a navy suit"></div>
<div class="quote-card">
  <div class="h" style="margin-top:42px;font-size:33px;font-weight:600;color:var(--red)">Testimonials</div>
  <svg style="margin-top:16px" width="52" height="52" viewBox="0 0 52 52"><circle cx="26" cy="26" r="26" fill="var(--orange)"/><path d="M15 32c0-7 3-11 8-13v4c-2 1-3 3-3 5h3v6h-8zM29 32c0-7 3-11 8-13v4c-2 1-3 3-3 5h3v6h-8z" fill="#fff"/></svg>
  <p style="margin:18px 64px 0;font-size:12.5px;line-height:20px">The feedback from our staff indicates they have benefited greatly from the course. There has been an overwhelming appreciation for the manner in which you conducted the course and presented all content. The staff also expressed their appreciation that all material presented was relevant to their day to day duties.</p>
  <p style="margin-top:22px;font-size:13px;line-height:19px;color:var(--red)">Daniel Reeve,<br><span style="color:var(--ink);font-size:12px">Northline Energy Group</span></p>
  <div class="btn-line" style="left:224px;top:340px;width:126px;height:34px">View All</div>
  <svg class="abs" style="left:26px;top:200px" width="10" height="18" viewBox="0 0 10 18"><path d="M8 2L2 9l6 7" stroke="#f7b59c" stroke-width="2" fill="none"/></svg>
  <svg class="abs" style="left:536px;top:200px" width="10" height="18" viewBox="0 0 10 18"><path d="M2 2l6 7-6 7" stroke="var(--orange)" stroke-width="2.5" fill="none"/></svg>
</div>

<!-- social -->
<div class="section-title" style="top:3866px">Keep social with VANTA</div>
<div class="post" style="left:89px"><div class="ph" role="img" aria-label="Magazine spread reviewing safety lights" style="background:linear-gradient(135deg,#2b2f55,#515a9c 60%,#d8d8e2)"></div><p>Great review of our Halo lights in the 'Out There' magazine (additional publication within the Coastline Fishing News magazine).</p><div class="meta"><span class="av">VANTA</span><span><b style="color:var(--ink);font-weight:500">VANTA</b><br>10 weeks ago</span><span class="sq"></span></div></div>
<div class="post" style="left:438px"><div class="ph" role="img" aria-label="Yellow car rescue tool on a keyring" style="background:linear-gradient(135deg,#f4f4f4,#f2c417 55%,#e9e9e9)"></div><p>Last night, Channel 8's "Fair Deal" examined car rescue tools. Something that hopefully none of us will ever have to use, but which...</p><div class="meta"><span class="av">VANTA</span><span><b style="color:var(--ink);font-weight:500">VANTA</b><br>10 weeks ago</span><span class="sq"></span></div></div>
<div class="post" style="left:787px"><div class="ph" role="img" aria-label="Officer in hi-vis vest wearing a body camera" style="background:linear-gradient(135deg,#c6e12a,#2c3a58 60%,#8fa34a)"></div><p>We've long been advocates of frontline police wearing Body Worn Video Cameras, whatever the brand or supplier.</p><div class="meta"><span class="av">VANTA</span><span><b style="color:var(--ink);font-weight:500">VANTA</b><br>10 weeks ago</span><span class="sq"></span></div></div>
<div class="btn-line" style="left:539px;top:4394px;width:121px;height:33px">View All</div>

<!-- footer -->
<svg class="footer" width="1200" height="525" viewBox="0 0 1200 525"><path d="M0 70 C300 40 500 40 600 40 C700 40 900 40 1200 70 L1200 525 L0 525Z" fill="var(--footer)"/></svg>
<div class="abs" style="left:538px;top:4496px;width:126px;height:126px;border-radius:50%;background:#fff;border:3px solid #ddd;display:flex;align-items:center;justify-content:center;font-family:'Rubik',sans-serif;font-weight:700;font-size:30px;color:var(--grey)">VANTA</div>
<div class="fcol" style="left:87px"><h4>Industries Served</h4><ul><li>Central Government</li><li>Local Government</li><li>Property Management</li><li>Health</li><li>Education</li><li>Libraries</li><li>Other Industries</li></ul></div>
<div class="fcol" style="left:351px;width:200px"><h4>Training</h4><ul style="line-height:19px"><li style="margin-bottom:8px">Situational Safety and Tactical Communications</li><li style="margin-bottom:8px">Compliance and Investigation Skills</li><li class="on" style="margin-bottom:8px">Front Counter Safety Training</li><li style="margin-bottom:8px">Firearms Safety Audit and Training</li><li>Open Courses</li></ul></div>
<div class="fcol" style="left:616px"><h4>Gear</h4><ul><li>Face Masks</li><li>Body Worn Video</li><li>Body Armour and Protective Vests</li><li>DryCore under Level 2 vests</li><li>Halo Safety Lights</li><li>Extendable Batons/Bite-sticks</li><li>Notebooks</li></ul></div>
<div class="fcol" style="left:896px;top:4714px;width:160px"><ul style="line-height:19px"><li style="margin-bottom:8px">ID Wallets</li><li style="margin-bottom:8px">RescueKey Safety Tools</li><li style="margin-bottom:8px">Stepwise Personal Defence Spray</li><li style="margin-bottom:8px">Duty belts</li><li style="margin-bottom:8px">Load Bearing Vests</li><li style="margin-bottom:8px">TetherWrap</li><li>Lone Worker Devices</li></ul></div>
<div class="fnav"><span class="on">Home</span><span>About</span><span>Online</span><span>Training</span><span>Advice</span><span>Contact</span></div>
<div class="fcall">Do you have a question? Call us on <b>0800 555 210</b></div>
<div class="bar">Copyright © 2021 VANTA. All Rights Reserved
  <span style="margin-left:auto;width:18px;height:18px;border-radius:50%;background:#fff"></span>
  <span style="margin-left:12px;width:18px;height:18px;background:#fff;border-radius:3px"></span>
</div>

</div>
</body>
</html>
```